Shampoo and Conditioner label design

We have a shampoo and conditioner line that we're looking to re-brand. We need the label re-designed to have a more appealing look. I have uploaded our logo and an example of our current design. We're looking for a design that advertises a more natural & and organic feel w/ natural, cool colors. A great bench mark which we're trying to emulate is Baobab Dew. They have great packaging for their products and they are attractive to a lot of people.

Target Market(s)

Natural hair. Ethnic hair.

Industry/Entity Type

Hair Care Product

Logo Text

Lumi Bright Locks

Colors

Designer to choose colors to be used in the design.

Requirements
Must have
• Must describe what the product does for the individual making the purchase.
• - hydrating and moisturizing
• - improves healthy shine
• - strengthens hair
• - organic ingredients
• - Sulfate Free
• - Paraben Free
Nice to have
• an appealing design. welcoming with warm, natural colors. informative

```html
<!DOCTYPE html>
<html lang="en">
<head>
<meta charset="utf-8">
<title>Lumi Bright Locks – Ultra Hydrating Shampoo Label</title>
<link rel="stylesheet" href="https://fonts.googleapis.com/css2?family=PT+Sans+Narrow:wght@400;700&family=Questrial&family=Arimo:ital,wght@0,400;0,700;1,700&display=swap">
<style>
  :root {
    --page-bg: #e6e7e8;
    --label-bg: #ffffff;
    --teal: #1a84a6;
    --band-teal: #2a8fb0;
    --ink: #222222;
    --grey-ink: #4a4a4a;
    --icon-grey: #8a8a8a;
  }
  * { margin: 0; padding: 0; box-sizing: border-box; }
  html, body { width: 1200px; height: 800px; overflow: hidden; background: var(--page-bg); }
  .label {
    position: absolute; left: 200px; top: 14px;
    width: 795px; height: 772px;
    background: var(--label-bg);
    font-family: "PT Sans Narrow", sans-serif;
    color: var(--ink);
  }
  .copy-block { position: absolute; left: 40px; width: 340px; font-size: 15.5px; line-height: 21px; }
  .copy-block strong { color: var(--teal); font-weight: 700; }
  .directions { top: 70px; }
  .warning { top: 154px; }
  .ingredients { top: 218px; }
  .certified { top: 470px; font-style: italic; font-size: 15px; }

  .maker { position: absolute; left: 40px; top: 548px; font-size: 15px; line-height: 21px; }
  .maker .brand-name { font-family: "Questrial", sans-serif; font-size: 19px; letter-spacing: 1px; color: var(--grey-ink); margin-bottom: 4px; }
  .maker .address { font-style: italic; }
  .maker .web { margin-top: 18px; }
  .maker .made-in { color: var(--teal); font-weight: 700; font-size: 18px; }

  .marks { position: absolute; left: 254px; top: 562px; display: flex; flex-direction: column; gap: 16px; }

  .band {
    position: absolute; left: 702px; top: 0; width: 91px; height: 408px;
    background: var(--band-teal);
  }
  .band-text {
    position: absolute; left: 702px; top: 0; width: 91px; height: 408px;
    display: flex; align-items: center; justify-content: center;
  }
  .band-text p {
    transform: rotate(-90deg); white-space: nowrap;
    font-family: "Arimo", sans-serif; color: #fff; font-size: 16px; line-height: 19px; letter-spacing: .5px;
  }
  .vertical-brand {
    position: absolute; left: 614px; top: 0; width: 80px; height: 408px;
    display: flex; align-items: flex-end; justify-content: center;
  }
  .vertical-brand span {
    display: block; transform: rotate(-90deg) translateX(0); transform-origin: center;
    white-space: nowrap; font-family: "Questrial", sans-serif; font-size: 28px; letter-spacing: 2px; color: var(--grey-ink);
    position: absolute; bottom: 150px;
  }
  .dotted-rule { position: absolute; left: 652px; top: 420px; width: 140px; border-top: 2px dotted #777; }

  .product { position: absolute; left: 440px; top: 470px; font-family: "Arimo", sans-serif; color: var(--grey-ink); }
  .product .new { font-weight: 700; font-style: italic; font-size: 22px; line-height: 22px; }
  .product .variant { font-size: 24px; line-height: 28px; }
  .product .name { font-family: "Questrial", sans-serif; font-size: 64px; line-height: 74px; color: var(--teal); font-weight: 700; letter-spacing: .5px; }
  .product .benefits { margin-top: 22px; font-size: 15.5px; line-height: 21px; }
  .product .net { margin-top: 22px; font-family: "PT Sans Narrow", sans-serif; font-size: 17px; }
</style>
</head>
<body>
  <main class="label">
    <p class="copy-block directions"><strong>DIRECTIONS:</strong> After shampooing, apply conditioner generously to hair. Massage gently into your hair and scalp, especially the ends. Wait 3-5 minutes. Rinse hair thoroughly.</p>
    <p class="copy-block warning"><strong>WARNING:</strong> Avoid contact with eyes. If contact occurs rinse immediately. Not intended for internal use.</p>
    <p class="copy-block ingredients"><strong>INGREDIENTS:</strong> *Organic Aloe Barbadenis Leaf Juice, Sodium C14-16 Olefin Sulfonate, Panthenol, Glycol Stearate, 1, 2-Hexanediol, Stearamidopropyl Dimethylamine, Polyquaternium-10, Potassium Sorbate, Lactic Acid, Althaea Officinalis (Marshmallow) Root Extract, Agave Americana Leaf Extract, Anthemis Nobilis (Chamomile) Flower Extract, Urtica Dioica (Nettle) Extract, Equisetum Arvense (Horsetail) Extract, Astrocaryum Murumuru Seed Butter, Passiflora Incarnata (Passionfruit) Seed Oil, Pentaclethra Macroloba Seed Oil, Caprylyl Glycol, Fragrance.</p>
    <p class="copy-block certified">*Certified Organic</p>

    <div class="maker">
      <p class="brand-name">LUMI BRIGHT LOCKS</p>
      <p>MANUFACTURED EXCLUSIVELY FOR</p>
      <p>Lumi Bright Locks</p>
      <p class="address">Maple Falls, TX 70010</p>
      <p class="web">www.lumibrightlocks.com</p>
      <p class="made-in">Made in USA</p>
    </div>

    <div class="marks">
      <svg width="28" height="28" viewBox="0 0 28 28" role="img" aria-label="Period after opening mark"><rect x="3" y="6" width="22" height="18" fill="none" stroke="var(--icon-grey)" stroke-width="2"/></svg>
      <svg width="28" height="28" viewBox="0 0 28 28" role="img" aria-label="Cruelty-free mark"><circle cx="14" cy="14" r="11" fill="none" stroke="var(--icon-grey)" stroke-width="2"/></svg>
      <svg width="28" height="28" viewBox="0 0 28 28" role="img" aria-label="Recyclable mark"><circle cx="14" cy="14" r="11" fill="none" stroke="var(--icon-grey)" stroke-width="2"/></svg>
    </div>

    <div class="band" role="img" aria-label="Teal band with soft floral swirl pattern"></div>
    <div class="band-text"><p>SPECIALLY FORMULATED<br>FOR ALL HAIR TYPES</p></div>
    <div class="vertical-brand"><span>LUMI BRIGHT LOCKS</span></div>
    <div class="dotted-rule"></div>

    <section class="product">
      <p class="new">NEW</p>
      <p class="variant">Ultra Hydrating</p>
      <h1 class="name">Shampoo</h1>
      <p class="benefits">Organic Aloe Vera &nbsp;•&nbsp; Improves healthy shine<br>Strengthens hair &nbsp;•&nbsp; Hydrating &amp; moisturizing<br>Natural mix of botanical oils</p>
      <p class="net">Net 16oz (473mL)</p>
    </section>
  </main>
</body>
</html>
```